Offshore Energy Projects Management Consultancy needs a business card design

Logo available. We provide teams to deliver engineering consultancy, project management and delivery teams mainly in the offshore renewables sector. The company is all about bringing the right people to a project to deliver the scope.

The business card will be used for all staff.

The business card should be quite simple, vibrant and uncluttered but convey experience, enthusiasm and integration.

Target Market(s)

Energy Project Developers and Tier 1 construction companies

Contact Information for Business Card

Logo should be on the back of the card. I'm happy for the designer to play with the colour of the logo and background colour.

Front of the card should convey all the must have information in a clear and professional manner but without being overly traditional.

Colors

Designer to choose colors to be used in the design.

Requirements
Must have
• Land Line Tel Number, Mobile Tel Number, Email, business address, web address.

```html
<!DOCTYPE html>
<html lang="en">
<head>
<meta charset="utf-8">
<title>Tidewater Delivery Partners – Business Card</title>
<link href="https://fonts.googleapis.com/css2?family=Montserrat:wght@400;500;600;700&display=swap" rel="stylesheet">
<style>
  :root {
    --backdrop: #1c1c1e;
    --card-white: #f7f8f9;
    --brand-blue: #1a82cf;
    --brand-blue-deep: #1466ad;
    --brand-blue-light: #2a9be0;
    --emboss-blue: #136bb0;
    --text-grey: #5e5f61;
    --rule-grey: #8a8b8d;
    --edge-blue: #2b8fdc;
  }
  * { margin: 0; padding: 0; box-sizing: border-box; }
  html, body {
    width: 1200px; height: 900px; overflow: hidden;
    background: var(--backdrop);
    font-family: "Montserrat", sans-serif;
  }
  .canvas { position: relative; width: 1200px; height: 900px; }

  .card {
    position: absolute; width: 630px; height: 360px;
    border-radius: 3px;
    box-shadow: 0 14px 30px rgba(0,0,0,.55);
  }

  /* Back of card */
  .card-back {
    left: 430px; top: 50px;
    background: linear-gradient(160deg, var(--brand-blue-light), var(--brand-blue) 60%, var(--brand-blue-deep));
    display: flex; align-items: center; justify-content: center;
  }
  .back-wordmark {
    display: flex; align-items: center; gap: 16px;
    color: var(--emboss-blue);
    font-weight: 700; font-size: 30px; letter-spacing: .5px;
    text-transform: uppercase;
  }
  .back-wordmark .mark-dot {
    width: 26px; height: 26px; border-radius: 50%;
    background: var(--emboss-blue);
  }

  /* Front of card */
  .card-front {
    left: 150px; top: 480px;
    background: var(--card-white);
    border-left: 5px solid var(--edge-blue);
    border-bottom: 3px solid var(--edge-blue);
  }
  .person { position: absolute; left: 50px; top: 70px; }
  .person-name { font-weight: 700; font-size: 24px; letter-spacing: .5px; }
  .person-name .first { color: var(--brand-blue-deep); }
  .person-name .last { color: var(--brand-blue-light); }
  .person-role { color: var(--text-grey); font-size: 14px; margin-top: 2px; }

  .front-wordmark {
    position: absolute; right: 40px; top: 78px;
    display: flex; align-items: center; gap: 10px;
    color: var(--text-grey);
    font-weight: 700; font-size: 19px; text-transform: uppercase;
  }
  .front-wordmark .mark-dot {
    width: 18px; height: 18px; border-radius: 50%;
    background: var(--brand-blue);
  }

  .divider {
    position: absolute; left: 50px; right: 40px; top: 150px;
    height: 1.5px; background: var(--rule-grey);
  }

  .contacts { position: absolute; left: 50px; top: 176px; list-style: none; }
  .contacts li {
    display: flex; align-items: center; gap: 14px;
    color: var(--text-grey); font-size: 16px; line-height: 30px;
  }
  .contacts svg { width: 14px; height: 14px; fill: var(--brand-blue); flex: none; }

  .address {
    position: absolute; right: 40px; bottom: 34px;
    text-align: right; color: var(--text-grey); font-size: 16px; line-height: 22px;
  }
</style>
</head>
<body>
<main class="canvas">
  <section class="card card-back" aria-label="Back of business card">
    <div class="back-wordmark"><span class="mark-dot"></span>Tidewater Delivery Partners</div>
  </section>

  <section class="card card-front" aria-label="Front of business card">
    <div class="person">
      <h1 class="person-name"><span class="first">JOHN</span> <span class="last">SMITH</span></h1>
      <p class="person-role">Manager</p>
    </div>

    <div class="front-wordmark"><span class="mark-dot"></span>Tidewater Delivery Partners</div>

    <div class="divider"></div>

    <ul class="contacts">
      <li>
        <svg viewBox="0 0 24 24" aria-hidden="true"><path d="M6.6 10.8a15.1 15.1 0 0 0 6.6 6.6l2.2-2.2c.3-.3.7-.4 1-.2 1.1.4 2.3.6 3.6.6.6 0 1 .4 1 1V20c0 .6-.4 1-1 1A17 17 0 0 1 3 4c0-.6.4-1 1-1h3.5c.6 0 1 .4 1 1 0 1.3.2 2.5.6 3.6.1.3 0 .7-.2 1z"/></svg>
        123-456-2100
      </li>
      <li>
        <svg viewBox="0 0 24 24" aria-hidden="true"><path d="M2 5h20v14H2z M3 6l9 7 9-7" /><path d="M2 5l10 8 10-8v14H2z" fill="var(--brand-blue)"/><path d="M3 5.5l9 6.5 9-6.5" stroke="#fff" stroke-width="1.5" fill="none"/></svg>
        youremail@mailhub.com
      </li>
      <li>
        <svg viewBox="0 0 24 24" aria-hidden="true"><circle cx="12" cy="12" r="10"/><path d="M2 12h20M12 2c3 3 3 17 0 20M12 2c-3 3-3 17 0 20" stroke="#fff" stroke-width="1.4" fill="none"/></svg>
        www.yourwebsite.com
      </li>
    </ul>

    <p class="address">Your address, city<br>state, ZIP 0000</p>
  </section>
</main>
</body>
</html>
```